Business Card Design Project

double sided, embossed, name & logo on front font sonsie one, back Name Marisol Venkamp, mobile 0468201934, Phone 73519086,
email marisol@brightspanservices.com, use sysbols on the back for example an envelope for email, a telephone for phone number etc.symbol slate grey writing navy blue

Industry/Entity Type

Business

```html
<!DOCTYPE html>
<html lang="en">
<head>
<meta charset="utf-8">
<title>Brightspan – Business Card</title>
<link rel="stylesheet" href="https://fonts.googleapis.com/css2?family=Sonsie+One&family=Open+Sans:ital,wght@0,400;1,400&display=swap">
<style>
  :root {
    --page-bg: #b9f3f5;
    --card-bg: #b9f3f5;
    --card-line: #1a1a1a;
    --logo-navy: #0d1a8c;
    --text-ink: #111111;
    --icon-tile: #111111;
    --icon-glyph: #ffffff;
    --social-tile-top: #6f86c4;
    --social-tile-bottom: #2f4f99;
    --art-teal: #4aa3b8;
    --art-sage: #b9c9a0;
    --art-amber: #e8b83a;
    --art-pink: #e46b9a;
    --art-blue: #6b9be0;
    --art-red: #e04848;
  }
  * { box-sizing: border-box; margin: 0; padding: 0; }
  html, body {
    width: 1200px; height: 927px; overflow: hidden;
    background: var(--page-bg);
  }
  .canvas { position: relative; width: 1200px; height: 927px; }

  .card-face {
    position: absolute; left: 275px; width: 654px;
    background: var(--card-bg);
    border: 1.5px solid var(--card-line);
  }
  .card-front { top: 96px; height: 374px; }
  .card-back { top: 468px; height: 375px; }

  .cleaning-art {
    position: absolute; border-radius: 14px; opacity: .85;
  }
  .art-spray-can { left: 112px; top: 65px; width: 131px; height: 66px; background: linear-gradient(90deg, var(--art-teal), #dfeff0); transform: rotate(-18deg); }
  .art-duster { left: 374px; top: 51px; width: 109px; height: 88px; background: linear-gradient(135deg, var(--art-sage), #b77a3a); }
  .art-sponge { left: 9px; top: 157px; width: 65px; height: 55px; background: linear-gradient(135deg, var(--art-amber), #9dbb3a); transform: rotate(20deg); }
  .art-squeegee { left: 140px; top: 242px; width: 111px; height: 77px; background: linear-gradient(90deg, var(--art-pink), #f3b5cc); }
  .art-spray-bottle { left: 393px; top: 237px; width: 61px; height: 92px; background: linear-gradient(180deg, var(--art-blue), #4aa0a0); }
  .art-bucket { left: 532px; top: 190px; width: 118px; height: 85px; background: linear-gradient(135deg, var(--art-red), #c6c9f5); }

  .brand-name {
    position: absolute; left: 0; right: 0; top: 148px;
    text-align: center;
    font-family: "Sonsie One", cursive;
    font-size: 52px; color: var(--logo-navy);
    letter-spacing: 1px;
  }

  .holder-name {
    position: absolute; left: 0; right: 0; top: 22px;
    text-align: center;
    font-family: "Open Sans", sans-serif; font-style: italic;
    font-size: 36px; color: var(--text-ink); letter-spacing: 1px;
  }
  .contact-list { position: absolute; left: 29px; top: 76px; list-style: none; }
  .contact-item {
    display: flex; align-items: center; height: 42px; margin-bottom: 14px;
    font-family: "Open Sans", sans-serif; font-size: 21px; color: var(--text-ink);
    letter-spacing: .5px;
  }
  .contact-email { font-style: italic; }
  .contact-icon {
    width: 42px; height: 42px; border-radius: 7px;
    background: var(--icon-tile); margin-right: 12px; flex: none;
    display: flex; align-items: center; justify-content: center;
  }
  .contact-icon svg { width: 28px; height: 28px; }
  .social-tile { background: linear-gradient(180deg, var(--social-tile-top), var(--social-tile-bottom)); border-radius: 2px; }
</style>
</head>
<body>
<main class="canvas">
  <section class="card-face card-front">
    <div class="cleaning-art art-spray-can" role="img" aria-label="Illustration of an air freshener spray can"></div>
    <div class="cleaning-art art-duster" role="img" aria-label="Illustration of a feather duster"></div>
    <div class="cleaning-art art-sponge" role="img" aria-label="Illustration of a cleaning sponge"></div>
    <div class="cleaning-art art-squeegee" role="img" aria-label="Illustration of a pink squeegee"></div>
    <div class="cleaning-art art-spray-bottle" role="img" aria-label="Illustration of a spray bottle"></div>
    <div class="cleaning-art art-bucket" role="img" aria-label="Illustration of a red bucket with soap bubbles"></div>
    <h1 class="brand-name">BRIGHTSPAN</h1>
  </section>

  <section class="card-face card-back">
    <h2 class="holder-name">Marisol Venkamp</h2>
    <ul class="contact-list">
      <li class="contact-item">
        <span class="contact-icon"><svg viewBox="0 0 24 24"><rect x="7" y="2" width="10" height="20" rx="2" fill="var(--icon-glyph)"/><rect x="9" y="5" width="6" height="5" fill="var(--icon-tile)"/><g fill="var(--icon-tile)"><circle cx="10" cy="13" r=".9"/><circle cx="12" cy="13" r=".9"/><circle cx="14" cy="13" r=".9"/><circle cx="10" cy="16" r=".9"/><circle cx="12" cy="16" r=".9"/><circle cx="14" cy="16" r=".9"/></g></svg></span>
        0468201934
      </li>
      <li class="contact-item">
        <span class="contact-icon"><svg viewBox="0 0 24 24" fill="var(--icon-glyph)"><path d="M3 9c0-3 4-4 9-4s9 1 9 4v1h-4V8H7v2H3z"/><path d="M6 12h12l2 8H4z"/><g fill="var(--icon-tile)"><circle cx="9" cy="15" r="1"/><circle cx="12" cy="15" r="1"/><circle cx="15" cy="15" r="1"/><circle cx="9" cy="18" r="1"/><circle cx="12" cy="18" r="1"/><circle cx="15" cy="18" r="1"/></g></svg></span>
        73519086
      </li>
      <li class="contact-item contact-email">
        <span class="contact-icon"><svg viewBox="0 0 24 24"><rect x="2" y="5" width="20" height="14" fill="var(--icon-glyph)"/><path d="M2 5l10 8 10-8M2 19l7-7M22 19l-7-7" fill="none" stroke="var(--icon-tile)" stroke-width="1.3"/></svg></span>
        marisol@brightspanservices.com
      </li>
      <li class="contact-item">
        <span class="contact-icon"><svg viewBox="0 0 24 24" fill="var(--icon-glyph)"><path d="M12 3l10 9h-3v9h-5v-6h-4v6H5v-9H2z"/></svg></span>
      </li>
      <li class="contact-item">
        <span class="contact-icon social-tile" aria-hidden="true"></span>
      </li>
    </ul>
  </section>
</main>
</body>
</html>
```